Saffron Lantern Court Business Card

I am looking for a business card desgined for my restaurant. It is an Indian restaurant, we are looking for something thats modern, yet traditional with the indian culture, we are looking for colors that match our logo. The logo is a design of the building with the name of the restaurant. for more information on the restaurant go to www.saffronlanterncourt.example

Industry/Entity Type

Indian Restaurant

Contact Information for Business Card

we are looking for somthing thats modern, yet traditional with the indian culture, we are looking for colors that match our logo. The logo is a design of the building with the name of the restaurant. for more information on the restaurant go to www.saffronlanterncourt.example

Requirements
Must have
• The logo that is attached,
• Name: Harvinder Oberoi,
• address of the restaurant: 7328 West Larkspur Rd, Phoenix, Arizona, 85213
• Phone: (602) 555-0147
• Fax: (602) 555-0193
• Restaurant Catering Banquet
• Website: www.SaffronLanternCourt.example
Nice to have
• wanted to get something that goes with the theme of the restaurant, which is traditional but also keep a very professional and modern touch

```html
<!DOCTYPE html>
<html lang="en">
<head>
<meta charset="utf-8">
<title>Saffron Lantern Court – Business Card</title>
<link rel="stylesheet" href="https://fonts.googleapis.com/css2?family=Source+Sans+3:wght@400;600&display=swap">
<style>
  :root {
    --backdrop: #3b3b3b;
    --paper: #ffffff;
    --peach: #fbc897;
    --brand-red: #b1262c;
    --accent-orange: #e8632a;
    --ink: #4a3a30;
  }
  * { box-sizing: border-box; margin: 0; padding: 0; }
  html, body {
    width: 1200px; height: 1200px; overflow: hidden;
    background: var(--backdrop);
    font-family: "Source Sans 3", Arial, sans-serif;
  }
  .card {
    position: absolute; left: 288px; width: 604px; height: 344px;
    box-shadow: 0 4px 10px rgba(0,0,0,.45);
    overflow: hidden;
  }
  .card--front { top: 222px; background: var(--peach); }
  .card--back { top: 624px; background: var(--peach); }

  .front__brand-panel {
    position: absolute; left: 0; top: 0; width: 302px; height: 100%;
    background: var(--paper);
  }
  .front__notch {
    position: absolute; left: 300px; top: 102px;
  }
  .brand-name {
    position: absolute; text-align: center;
    color: var(--brand-red); font-weight: 600;
    text-transform: uppercase; line-height: 1.05;
  }
  .front__brand-panel .brand-name {
    left: 0; width: 302px; top: 122px; font-size: 32px; letter-spacing: 1px;
  }
  .card--back .brand-name {
    left: 0; width: 604px; top: 118px; font-size: 46px; letter-spacing: 2px;
  }
  .contact {
    position: absolute; left: 334px; top: 102px; color: var(--ink);
  }
  .contact__name {
    color: var(--brand-red); font-size: 22px; font-weight: 400; margin-bottom: 12px;
  }
  .contact__line {
    display: flex; align-items: center; gap: 8px;
    font-size: 15.5px; line-height: 20px;
  }
  .contact__line svg { width: 14px; height: 14px; flex: none; }
  .contact__address { margin-top: 11px; font-size: 15.5px; line-height: 20px; }
</style>
</head>
<body>
  <section class="card card--front">
    <div class="front__brand-panel">
      <p class="brand-name">Saffron<br>Lantern<br>Court</p>
    </div>
    <svg class="front__notch" width="16" height="32" viewBox="0 0 16 32" aria-hidden="true">
      <polygon points="0,0 16,16 0,32" fill="var(--paper)"/>
    </svg>
    <div class="contact">
      <p class="contact__name">Harvinder Oberoi</p>
      <p class="contact__line">
        <svg viewBox="0 0 14 14" aria-hidden="true"><path d="M1 5 Q7 0 13 5 L11 7 L9 5.5 L5 5.5 L3 7 Z M3 8 H11 V12 H3 Z" fill="var(--accent-orange)"/></svg>
        (602) 555-0147
      </p>
      <p class="contact__line">
        <svg viewBox="0 0 14 14" aria-hidden="true"><rect x="4" y="1" width="6" height="4" fill="var(--accent-orange)"/><rect x="1" y="5" width="12" height="5" rx="1" fill="var(--accent-orange)"/><rect x="4" y="9" width="6" height="4" fill="var(--accent-orange)"/></svg>
        (602) 555-0193
      </p>
      <p class="contact__line">
        <svg viewBox="0 0 14 14" aria-hidden="true"><g fill="none" stroke="var(--accent-orange)" stroke-width="1.2"><circle cx="7" cy="7" r="5.5"/><ellipse cx="7" cy="7" rx="2.5" ry="5.5"/><line x1="1.5" y1="7" x2="12.5" y2="7"/></g></svg>
        www.SaffronLanternCourt.example
      </p>
      <p class="contact__address">7328 West Larkspur Rd<br>Phoenix, Arizona, 85213</p>
    </div>
  </section>

  <section class="card card--back">
    <p class="brand-name">Saffron<br>Lantern<br>Court</p>
  </section>
</body>
</html>
```